Bourbon label design for bourbon brand. Looking to freshen our current label.

I need a Bourbon label design for our rebranded Bourbon bottle. Label should include picture of our horse and our logo on the bottle. Front Label is 3.5 inches wide and 6 inches tall, back label is 4 inches tall and 3 inches wide. Back label can be a simple plain logo like the one in the brief. I have included a design of our current bottle and label. We want to stay close to the current color schemes but want a fresh rebrand of the design. The label needs to be the correct size on a tall bottle like pictured.

Target Market(s)

Our Bourbon members, 30-50 year old males

Requirements
Must have
• Picture of our horse, our B logo , straight Bourbon whiskey on the front. Room to edit text on the back label.

```html
<!DOCTYPE html>
<html lang="en">
<head>
<meta charset="utf-8">
<title>Nightfall Straight Bourbon Whiskey – Front Label</title>
<link rel="stylesheet" href="https://fonts.googleapis.com/css2?family=Oswald:wght@400;500&family=Rye&display=swap">
<style>
  :root {
    --backdrop: #eeeeee;
    --label-black: #0b0b0b;
    --ink-white: #f4f4f4;
    --rule-grey: #d9d9d9;
    --photo-dark: #141414;
    --photo-mid: #5a5a5a;
    --photo-light: #a9a9a9;
  }
  * { margin: 0; padding: 0; box-sizing: border-box; }
  html, body {
    width: 849px;
    height: 1200px;
    overflow: hidden;
    background: var(--backdrop);
  }
  .canvas {
    position: relative;
    width: 849px;
    height: 1200px;
  }
  .front-label {
    position: absolute;
    left: 112px;
    top: 56px;
    width: 625px;
    height: 1088px;
    background: var(--label-black);
    color: var(--ink-white);
    font-family: "Oswald", "Arial Narrow", sans-serif;
  }
  .label-frame {
    position: absolute;
    left: 34px;
    top: 113px;
    width: 557px;
    height: 949px;
  }
  .est-tab {
    position: absolute;
    left: 50%;
    top: 75px;
    transform: translateX(-50%);
    width: 150px;
    height: 38px;
    border: 2px solid var(--rule-grey);
    background: var(--label-black);
    display: flex;
    align-items: center;
    justify-content: center;
    font-size: 19px;
    letter-spacing: 2px;
    font-weight: 500;
  }
  .horse-photo {
    position: absolute;
    left: 162px;
    top: 144px;
    width: 300px;
    height: 394px;
    background: radial-gradient(ellipse at 45% 40%, var(--photo-light) 0%, var(--photo-mid) 40%, var(--photo-dark) 75%, var(--label-black) 100%);
  }
  .brand-mark {
    position: absolute;
    left: 0;
    right: 0;
    top: 548px;
    display: flex;
    align-items: center;
    justify-content: center;
    gap: 14px;
  }
  .brand-mark .dot {
    width: 70px;
    height: 70px;
    border-radius: 50%;
    background: var(--ink-white);
  }
  .brand-mark .name {
    font-size: 40px;
    font-weight: 500;
    letter-spacing: 3px;
  }
  .wordmark {
    position: absolute;
    left: 0;
    right: 0;
    top: 724px;
    text-align: center;
    font-family: "Rye", Georgia, serif;
    font-size: 68px;
    letter-spacing: 1px;
    line-height: 1.4;
  }
  .spirit-type {
    position: absolute;
    left: 0;
    right: 0;
    top: 840px;
    text-align: center;
    font-size: 32px;
    letter-spacing: 2.5px;
    line-height: 1.3;
  }
  .spec-table {
    position: absolute;
    left: 81px;
    top: 906px;
    width: 462px;
    height: 94px;
    display: grid;
    grid-template-columns: 1fr 1fr 1fr;
    border-top: 2px solid var(--rule-grey);
    border-bottom: 2px solid var(--rule-grey);
  }
  .spec-table::before,
  .spec-table::after {
    content: "";
    position: absolute;
    top: 8px;
    bottom: 8px;
    width: 2px;
    background: var(--rule-grey);
  }
  .spec-table::before { left: 0; }
  .spec-table::after { right: 0; }
  .spec {
    display: flex;
    flex-direction: column;
    align-items: center;
    justify-content: center;
    line-height: 1.1;
  }
  .spec + .spec { border-left: 2px solid var(--rule-grey); }
  .spec-name { font-size: 16px; letter-spacing: 1px; }
  .spec-value { font-size: 42px; letter-spacing: 1px; }
</style>
</head>
<body>
<main class="canvas">
  <section class="front-label">
    <svg class="label-frame" viewBox="0 0 557 949" width="557" height="949" aria-hidden="true">
      <rect x="1" y="1" width="555" height="947" fill="none" stroke="#d9d9d9" stroke-width="2"/>
      <rect x="9" y="9" width="539" height="931" fill="none" stroke="#d9d9d9" stroke-width="2"/>
    </svg>
    <div class="est-tab">EST 2016</div>
    <div class="horse-photo" role="img" aria-label="Black and white photograph of the brand's racehorse galloping head-on with its jockey"></div>
    <div class="brand-mark">
      <span class="dot"></span>
      <span class="name">NIGHTFALL</span>
    </div>
    <h1 class="wordmark">NIGHTFALL</h1>
    <p class="spirit-type">STRAIGHT BOURBON WHISKEY</p>
    <div class="spec-table">
      <div class="spec"><span class="spec-name">BARREL NO</span><span class="spec-value">28</span></div>
      <div class="spec"><span class="spec-name">AGED</span><span class="spec-value">10</span></div>
      <div class="spec"><span class="spec-name">ALC. VOL</span><span class="spec-value">66%</span></div>
    </div>
  </section>
</main>
</body>
</html>
```